BrXpertz Business Cards for SME Experts

We need a business card for a new company based in Clearwater FL called Kestrel of Merit. KoM is your access to on-demand subject matter experts. The final design should be very clean communicating innovation and expertise. Our logo design is attached.

The Information Age has affected the workforce in that automation and computerization have resulted in higher productivity coupled with net job loss of many knowledgeable employees. Combined with the creation of the internet and search capabilities, the disintermediation of the value chain of Subject Matter Experts (SME) has happened. We no longer need to work through traditional consulting firms for all consulting needs, instead the direct access to the SME, through a leaner and lower cost model is what the market is demanding.
BrXpertz is a new marketplace to buy consulting services. The business model is that all consultants (subject matter experts) can become a consulting resource in the marketplace following our guidelines. The consumer can now easily access consultants that they could not find easily before.
In much the way an Zyla car can be identified and requested, so can a BrXpertz Consultant. Each consultant can be identified by: location, expertise, billing rate, and prior experience rating.
By seamlessly connecting consultants to requesters through a new Kestrel of Merit marketplace, you now will have an easy to use and quicker turnaround to request and staff your consulting needs. Leveraging the KoM app, you can access the subject matter expert you need for your business requirement.

Target Market(s)

Small and medium sized companies; non-profits

Industry/Entity Type

Business Consultant

Contact Information for Business Card

Name
website
email address
Logo
mailing address (debating if I really need...)
twitter
LinkedIn

Requirements
Must have
• the logo I have included in the design; want the colors to be consistent with the logo design

```html
<!DOCTYPE html>
<html lang="en">
<head>
<meta charset="utf-8">
<title>Kestrel of Merit – Business Card</title>
<link rel="stylesheet" href="https://fonts.googleapis.com/css2?family=Open+Sans:wght@400;600;700&display=swap">
<style>
  :root {
    --backdrop: #c9c9c9;
    --card-white: #ffffff;
    --brand-navy: #272a6b;
    --brand-cyan: #1ba3c6;
    --band-dark: #111530;
    --band-dark-2: #161b3b;
    --ghost: #e6e8ef;
    --text-light: #f2f4f8;
  }
  * { box-sizing: border-box; margin: 0; padding: 0; }
  html, body {
    width: 1200px; height: 900px; overflow: hidden;
    background: var(--backdrop);
    font-family: "Open Sans", sans-serif;
  }
  .canvas { position: relative; width: 1200px; height: 900px; }
  .card {
    position: absolute; left: 160px; top: 160px;
    width: 880px; height: 580px;
    border-radius: 40px; overflow: hidden;
    background: var(--card-white);
    box-shadow: 0 14px 30px rgba(0,0,0,0.25);
  }
  .card__ghost-mark {
    position: absolute; right: -110px; top: 20px;
    width: 270px; height: 270px; border-radius: 50%;
    border: 16px solid var(--ghost);
  }
  .brand {
    position: absolute; left: 56px; top: 62px;
    display: flex; align-items: center; gap: 30px;
  }
  .brand__circle {
    width: 170px; height: 170px; border-radius: 50%;
    border: 9px solid var(--brand-navy);
  }
  .brand__name {
    font-size: 46px; font-weight: 700; color: var(--brand-navy);
    letter-spacing: 0.5px; line-height: 1;
  }
  .card__stripe {
    position: absolute; left: 0; top: 286px; width: 100%; height: 16px;
    background: var(--brand-cyan);
  }
  .card__band {
    position: absolute; left: 0; top: 302px; width: 100%; height: 278px;
    background: linear-gradient(180deg, var(--band-dark-2), var(--band-dark));
  }
  .holder {
    position: absolute; left: 58px; top: 318px;
    font-size: 28px; font-weight: 600; color: var(--brand-cyan);
    line-height: 36px;
  }
  .contacts {
    position: absolute; left: 58px; top: 366px;
    list-style: none;
  }
  .contacts__item {
    display: flex; align-items: center; gap: 14px;
    height: 38px;
    font-size: 22px; line-height: 1; color: var(--text-light);
    white-space: nowrap;
  }
  .contacts__icon { width: 30px; height: 30px; flex: none; }
</style>
</head>
<body>
<main class="canvas">
  <section class="card" aria-label="Kestrel of Merit business card">
    <div class="card__ghost-mark" aria-hidden="true"></div>

    <div class="brand">
      <div class="brand__circle" aria-hidden="true"></div>
      <span class="brand__name">Kestrel of Merit</span>
    </div>

    <div class="card__stripe"></div>
    <div class="card__band"></div>

    <h1 class="holder">Nolan Avery</h1>

    <ul class="contacts">
      <li class="contacts__item">
        <svg class="contacts__icon" viewBox="0 0 30 30" fill="none" stroke="var(--brand-cyan)" stroke-width="2">
          <circle cx="15" cy="15" r="13"/>
          <circle cx="15" cy="15" r="8.5" stroke-width="1.5"/>
          <ellipse cx="15" cy="15" rx="3.5" ry="8.5" stroke-width="1.5"/>
          <line x1="6.5" y1="15" x2="23.5" y2="15" stroke-width="1.5"/>
        </svg>
        www.kestrelofmerit.com
      </li>
      <li class="contacts__item">
        <svg class="contacts__icon" viewBox="0 0 30 30" fill="none" stroke="var(--brand-cyan)" stroke-width="2">
          <circle cx="15" cy="15" r="13"/>
          <text x="15" y="20.5" text-anchor="middle" font-family="Open Sans, sans-serif" font-size="16" font-weight="700" fill="var(--brand-cyan)" stroke="none">@</text>
        </svg>
        nolan@kestrelofmerit.com
      </li>
      <li class="contacts__item">
        <svg class="contacts__icon" viewBox="0 0 30 30" fill="none" stroke="var(--brand-cyan)" stroke-width="2">
          <circle cx="15" cy="15" r="13"/>
        </svg>
        chirpline/kestrelofmerit
      </li>
      <li class="contacts__item">
        <svg class="contacts__icon" viewBox="0 0 30 30" fill="none" stroke="var(--brand-cyan)" stroke-width="2">
          <circle cx="15" cy="15" r="13"/>
        </svg>
        linkfolio/kestrelofmerit
      </li>
      <li class="contacts__item">
        <svg class="contacts__icon" viewBox="0 0 30 30" fill="none" stroke="var(--brand-cyan)" stroke-width="2">
          <circle cx="15" cy="15" r="13"/>
          <path d="M15 23 C11 18 10 15.5 10 13 a5 5 0 0 1 10 0 c0 2.5 -1 5 -5 10z" stroke-width="1.8"/>
          <circle cx="15" cy="13" r="1.8" stroke-width="1.5"/>
        </svg>
        location, mailing address
      </li>
    </ul>
  </section>
</main>
</body>
</html>
```